women's junior contemporary apparel company.
We are looking for a business card that represents our urban design aesthetic. We would like to keep it simple and modern/contemporary.
the name of the company is 'v-lanza'.

we've attached a font style but you are not limited solely to use this font. All suggestions are welcomed.

```html
<!DOCTYPE html>
<html lang="en">
<head>
<meta charset="utf-8">
<title>v-lanza business card</title>
<link rel="stylesheet" href="https://fonts.googleapis.com/css2?family=Comic+Neue:wght@400;700&display=swap">
<style>
  :root {
    --surface: #1e1e1e;
    --card: #f6f6ec;
    --ink: #3a3a3a;
    --accent: #f2c94c;
    --rule: #f3d98a;
  }
  * { box-sizing: border-box; margin: 0; padding: 0; }
  html, body { width: 1200px; height: 1000px; overflow: hidden; }
  body {
    background: var(--surface);
    font-family: "Comic Neue", "Comic Sans MS", cursive;
    color: var(--ink);
    display: flex;
    flex-direction: column;
    align-items: center;
    justify-content: center;
    gap: 60px;
  }
  .card {
    position: relative;
    width: 700px;
    height: 400px;
    background: var(--card);
  }
  .card--back {
    display: flex;
    align-items: center;
    justify-content: center;
  }
  .brand {
    font-weight: 700;
    color: var(--ink);
    letter-spacing: 1px;
  }
  .card--back .brand { font-size: 150px; }
  .card--front .brand {
    position: absolute;
    top: 34px;
    right: 70px;
    font-size: 64px;
  }
  .rule {
    position: absolute;
    left: 0;
    right: 0;
    height: 1px;
    background: var(--rule);
  }
  .rule--top { top: 148px; }
  .rule--bottom { top: 344px; }
  .person {
    position: absolute;
    top: 112px;
    left: 50px;
  }
  .person__name {
    font-size: 30px;
    font-weight: 700;
    color: var(--accent);
    letter-spacing: 1px;
  }
  .person__role {
    font-size: 16px;
    letter-spacing: 6px;
    margin-top: 2px;
  }
  .contact {
    position: absolute;
    top: 190px;
    left: 50px;
    list-style: none;
    font-size: 20px;
    line-height: 1.45;
  }
  .label {
    color: var(--accent);
    font-size: 17px;
    margin-right: 6px;
  }
  .location {
    position: absolute;
    top: 292px;
    right: 70px;
    font-size: 20px;
    line-height: 1.2;
  }
</style>
</head>
<body>
  <section class="card card--back">
    <span class="brand">v-lanza</span>
  </section>

  <section class="card card--front">
    <span class="brand">v-lanza</span>
    <div class="rule rule--top"></div>
    <div class="person">
      <p class="person__name">Mira Solano</p>
      <p class="person__role">Designer</p>
    </div>
    <ul class="contact">
      <li><span class="label">Mob.</span>012-555-019</li>
      <li><span class="label">Email.</span>hello@vlanza.com</li>
    </ul>
    <p class="location"><span class="label">Loc.</span>45 Elm St.,<br>nova</p>
    <div class="rule rule--bottom"></div>
  </section>
</body>
</html>
```